依頼詳細
・リスティングでの運用を考えているので、コンバージョンを期待できるデザイン、サイト構成
・レスポンシブでコーディングするためそれを念頭に置いたデザイン
・提案デザインはスマホ、PC両画面でお願いします。
・サイト構成も変わる可能性が高いので、HTMLやCSSでの変更が容易なデザイン
(メニューなどを画像にしないetc)
・奇抜さよりも安心感
・病院関係のウェブサイト構築実績のある方歓迎
・病院の場所はみなとみらいです。
ページ数
2ページ
希望イメージ
シンプル 複雑
単色 カラフル
暗い 明るい
日常 高級
遊び心 厳粛
未来的 伝統的
女性的 男性的
希望する色
青系、水色系、緑系、黄・オレンジ系
納品ファイル
• 高解像度JPG (.jpg)
• フォトショップ形式 (.psd)
補足説明
■ 補足
--------------------------------
・基本HTMLコーディングは無しで構いませんが、
対応可能な方はコーディング作業についてもお見積ください。

・採用された方は今後も引続き作業をお願いすることになると思います。

■ 注意点

・お渡しできる素材は、サイトマップのみとなります
・病院名なども決まっていないので、ロゴなどは仮のもので構いません。
・サイトの中の文言なども仮の文章で構いません。
・写真素材も仮のもので構いません。
(最終的には素材もしくは撮影した写真に入れ替えます。)

○想定サイトマップ
診療科目
病院案内
├ ご挨拶・理念
├ 施設案内
└ ドクター紹介
アクセス
よくある質問
採用情報
サイトマップ
お問い合わせ
予約

※サイト構成も決定ではないので提案頂く形でも構いません。

参考サイト
http://www.rokuha-dental.com/
https://www.clinic-yuzumi.com/
ウェブサイトの構成が、内科・整形外科・歯科の診療科目を一つのサイトで集患する形に変更になりました。大きい枠組みで変わるのはこれ以降はないと思います。素敵なデザイナー様との出会いを期待しております。
お盆に入ってしまうので、締切を延長させていただきました。今後も数々の案件抱えておりますので、長いお付き合いができるデザイナー様との出会いを期待しております。
たくさんのご応募、誠にありがとうございます!

これから社内で選定を行います。
一週間以内には決定できると思いますので少々お待ち頂ければと思います。
よろしくお願いいたします。
デザインの選定に時間がかかっておりますので、決定までもう少々お待ち頂ければと思います。申し訳ありません、よろしくお願いいたします。
■ 選んだ理由

シンプルにデザインがまとまっていたところと、アイコンなどを使いぱっと見た時のわかりやすさ、写真を変更しても違和感なくマッチしそうな点などを評価させていただきました。

■ 提案者全員のお礼・コメント

この度は弊社コンペにご参加頂き誠にありがとうございます。
優れたデザイン・提案を多数頂きとても感謝しております。

ギリギリまでどの提案を採用させていただくか迷いましたが、
今回はこのような結果となりました。

またの機会がありましたら、またぜひご参加頂ければ幸いです。
ありがとうございました。

```html
<!DOCTYPE html>
<html lang="ja">
<head>
<meta charset="utf-8">
<title>港みらいクリニック</title>
<link href="https://fonts.googleapis.com/css2?family=Noto+Sans+JP:wght@400;500;700&family=Roboto:wght@400;500;700&display=swap" rel="stylesheet">
<style>
:root{
  --teal:#2bb3c0;
  --teal-dark:#1f97a3;
  --teal-pale:#e8f6f7;
  --blue:#2f6fd6;
  --orange:#f08a1c;
  --text:#333;
  --muted:#777;
  --line:#d7e6e8;
  --white:#fff;
}
*{box-sizing:border-box;margin:0;padding:0}
html,body{width:1200px;height:2596px;overflow:hidden}
body{font-family:"Noto Sans JP",sans-serif;color:var(--text);background:var(--white);font-size:14px;position:relative}
.top-strip{height:28px;background:var(--teal);color:var(--white);font-size:12px;line-height:28px;padding-left:20px}
.site-header{height:102px;display:flex;align-items:center;justify-content:space-between;padding:0 60px 0 100px}
.brand{display:flex;align-items:center;gap:14px}
.brand-dot{width:54px;height:54px;border-radius:50%;background:var(--teal)}
.brand-name{font-size:30px;font-weight:700;color:var(--teal-dark);line-height:1.1}
.brand-sub{font-size:13px;color:var(--muted);margin-top:4px;letter-spacing:.1em}
.header-contact{display:flex;align-items:center;gap:24px}
.hours{font-size:11px;color:var(--muted);line-height:1.6}
.phone{display:flex;flex-direction:column;align-items:flex-start}
.phone-label{font-size:11px;color:var(--muted)}
.phone-num{display:flex;align-items:center;gap:6px;font-family:"Roboto",sans-serif;font-size:32px;font-weight:700;color:var(--orange);white-space:nowrap}
.hero{height:418px;display:flex}
.hero-panel{flex:1;position:relative}
.hero-panel:nth-child(1){background:linear-gradient(160deg,#f3f6f8,#c9d8df)}
.hero-panel:nth-child(2){background:linear-gradient(160deg,#9fc5d3,#3f7f98)}
.hero-panel:nth-child(3){background:linear-gradient(160deg,#eef1f2,#b9c7cc)}
.hero-label{position:absolute;left:50%;bottom:44px;transform:translateX(-50%);width:280px;height:100px;background:rgba(255,255,255,.92);text-align:center;padding-top:16px}
.hero-label strong{display:block;font-size:40px;font-weight:500;color:var(--teal-dark);line-height:1.1}
.hero-label span{font-size:12px;color:var(--muted);letter-spacing:.05em}
.main-nav{height:56px;background:var(--teal);display:flex;justify-content:center}
.main-nav a{color:var(--white);text-decoration:none;font-size:14px;display:flex;align-items:center;padding:0 26px;border-right:1px solid rgba(255,255,255,.35)}
.main-nav a:first-child{border-left:1px solid rgba(255,255,255,.35)}
.greeting{height:400px;display:flex;padding:30px 110px 0 140px;gap:40px;background:linear-gradient(#f6f6f6,#fff 40%)}
.greeting-photo{width:240px;height:340px;background:linear-gradient(#eef2f4,#c8d3d9)}
.greeting-body{flex:1;padding-top:20px}
.eyebrow{font-size:13px;color:var(--muted)}
.greeting h2{font-size:27px;font-weight:700;color:var(--teal-dark);margin:4px 0 22px}
.greeting p{font-size:13px;line-height:2.1;color:#555}
.btn-more{display:block;margin:30px 0 0 auto;width:230px;height:52px;background:var(--blue);color:var(--white);font-size:15px;text-align:center;line-height:52px;text-decoration:none;border-radius:3px}
.departments{height:686px;background:var(--teal-pale);padding-top:28px;text-align:center}
.section-title{font-size:28px;color:var(--teal-dark);font-weight:500}
.section-lead{font-size:12px;color:var(--muted);margin:8px 0 34px}
.dept-cards{display:flex;justify-content:center;gap:48px}
.dept-card{width:296px;background:var(--white);border:2px solid var(--teal);text-align:left;padding:14px 14px 16px}
.dept-card h3{font-size:22px;font-weight:500;color:var(--teal-dark)}
.dept-card h3 span{font-size:12px;color:var(--text);margin-left:6px}
.dept-photo{height:220px;margin:12px 0 14px}
.dept-card:nth-child(1) .dept-photo{background:linear-gradient(#dde6ea,#a7b9c1)}
.dept-card:nth-child(2) .dept-photo{background:linear-gradient(#c7dce4,#6f97a8)}
.dept-card:nth-child(3) .dept-photo{background:linear-gradient(#eef1f2,#b6c3c8)}
.dept-card p{font-size:12px;line-height:2;color:#555;height:72px}
.dept-btn{display:flex;justify-content:center;align-items:center;gap:14px;margin-top:16px;height:46px;background:var(--teal);color:var(--white);font-size:14px;text-decoration:none}
.news{height:170px;background:var(--teal);display:flex;padding:18px 100px 0 140px;gap:60px}
.news-head{color:var(--white);width:160px}
.news-head h2{font-size:26px;font-weight:500}
.news-head span{font-size:12px}
.news-list{flex:1;list-style:none}
.news-list li{display:flex;gap:30px;font-size:12px;line-height:18px;color:var(--white);padding:4px 0;border-bottom:1px dashed rgba(255,255,255,.45)}
.news-list time{font-family:"Roboto",sans-serif;width:90px}
.site-footer{height:668px;display:flex;padding:30px 100px 0 140px;gap:50px}
.footer-info{width:360px}
.footer-info .brand-dot{width:48px;height:48px}
.footer-info .brand-name{font-size:26px}
.footer-dept{margin:22px 0 10px;font-size:15px;font-weight:700;color:var(--teal-dark)}
.footer-dept small{display:block;font-size:13px;font-weight:400;color:var(--text)}
.footer-info p{font-size:12px;line-height:1.8;color:#555}
.footer-info .phone-num{font-size:38px;margin:6px 0 14px}
.schedule{width:100%;border-collapse:collapse;font-size:12px;background:var(--teal-pale)}
.schedule th,.schedule td{border:1px solid var(--white);text-align:center;height:30px}
.schedule thead th{background:var(--teal);color:var(--white);font-weight:500}
.schedule td{color:var(--teal-dark)}
.map{flex:1;height:610px;background:linear-gradient(135deg,#eef0e8,#dfe6ee 50%,#cfe0ec);border:1px solid var(--line)}
.footer-nav{position:absolute;left:0;top:2528px;width:1200px;height:44px;background:var(--teal);display:flex;justify-content:center}
.footer-nav a{color:var(--white);text-decoration:none;font-size:12px;display:flex;align-items:center;padding:0 22px;border-right:1px solid rgba(255,255,255,.35)}
.copyright{position:absolute;left:0;top:2572px;width:1200px;height:24px;background:var(--teal-dark);color:var(--white);font-size:11px;text-align:center;line-height:24px}
</style>
</head>
<body>
<div class="top-strip">内科・整形外科・歯科｜港央駅すぐの地域密着クリニックです</div>

<header class="site-header">
  <div class="brand">
    <div class="brand-dot"></div>
    <div>
      <div class="brand-name">港みらいクリニック</div>
      <div class="brand-sub">内科・整形外科・歯科</div>
    </div>
  </div>
  <div class="header-contact">
    <div class="hours">診療時間｜午前 9:00〜12:30　午後 14:00〜18:00<br>休診日｜日曜・祝日<br>〒231-0099 横浜市中区港央町4-2-8</div>
    <div class="phone">
      <span class="phone-label">お問い合わせ・予約受付</span>
      <span class="phone-num"><svg width="28" height="28" viewBox="0 0 24 24"><path fill="#f08a1c" d="M6.6 10.8a15 15 0 0 0 6.6 6.6l2.2-2.2a1 1 0 0 1 1-.25 11.4 11.4 0 0 0 3.6.57 1 1 0 0 1 1 1V20a1 1 0 0 1-1 1A17 17 0 0 1 3 4a1 1 0 0 1 1-1h3.5a1 1 0 0 1 1 1c0 1.250.2 2.45.57 3.57a1 1 0 0 1-.25 1z"/></svg>045-555-0132</span>
    </div>
  </div>
</header>

<section class="hero">
  <div class="hero-panel" role="img" aria-label="内科の診察風景の写真"><div class="hero-label"><strong>内科</strong><span>Internal medicine</span></div></div>
  <div class="hero-panel" role="img" aria-label="整形外科の手術風景の写真"><div class="hero-label"><strong>整形外科</strong><span>Plastic surgery</span></div></div>
  <div class="hero-panel" role="img" aria-label="歯科の診療風景の写真"><div class="hero-label"><strong>歯科</strong><span>Dentistry</span></div></div>
</section>

<nav class="main-nav">
  <a href="#"><svg width="18" height="18" viewBox="0 0 24 24"><path fill="#fff" d="M12 3 2 12h3v8h5v-5h4v5h5v-8h3z"/></svg></a>
  <a href="#">診療案内</a><a href="#">病院案内</a><a href="#">アクセス</a><a href="#">よくある質問</a><a href="#">採用情報</a><a href="#">サイトマップ</a><a href="#">お問い合わせ</a><a href="#">予約</a>
</nav>

<section class="greeting">
  <div class="greeting-photo" role="img" aria-label="白衣の院長の写真"></div>
  <div class="greeting-body">
    <div class="eyebrow">院長あいさつ</div>
    <h2>地域の通いやすい病院を地域の皆さまへ貢献したい</h2>
    <p>当院は内科・整形外科・歯科をひとつの場所でご案内できるクリニックです。日々の体調の不安から、からだの痛み、お口の健康まで、どなたにも気軽にご相談いただける環境づくりを心がけています。地域の皆さまの暮らしに寄り添い、安心して通っていただける医療をこれからもお届けします。</p>
    <a class="btn-more" href="#">続きはこちら</a>
  </div>
</section>

<section class="departments">
  <h2 class="section-title">診療案内</h2>
  <p class="section-lead">港みらいクリニックでは内科・整形外科・歯科の3つの診療科でみなさまの健康を支えています</p>
  <div class="dept-cards">
    <article class="dept-card">
      <h3>内科<span>Internal medicine</span></h3>
      <div class="dept-photo" role="img" aria-label="内科の診察室の写真"></div>
      <p>かぜや発熱、生活習慣病など日常のからだの不調を幅広く診療します。健康診断もお気軽にどうぞ。</p>
      <a class="dept-btn" href="#">詳しくはこちら <svg width="30" height="10" viewBox="0 0 30 10"><path d="M0 8h28L22 2" fill="none" stroke="#fff" stroke-width="1.5"/></svg></a>
    </article>
    <article class="dept-card">
      <h3>整形外科<span>Plastic surgery</span></h3>
      <div class="dept-photo" role="img" aria-label="整形外科の手術室の写真"></div>
      <p>腰や膝の痛み、けが、スポーツ障害など骨と関節のお悩みに丁寧に対応いたします。</p>
      <a class="dept-btn" href="#">詳しくはこちら <svg width="30" height="10" viewBox="0 0 30 10"><path d="M0 8h28L22 2" fill="none" stroke="#fff" stroke-width="1.5"/></svg></a>
    </article>
    <article class="dept-card">
      <h3>歯科<span>Dentistry</span></h3>
      <div class="dept-photo" role="img" aria-label="歯科の診療台の写真"></div>
      <p>虫歯や歯周病の治療から定期検診、予防ケアまで、お口の健康を長く守ります。</p>
      <a class="dept-btn" href="#">詳しくはこちら <svg width="30" height="10" viewBox="0 0 30 10"><path d="M0 8h28L22 2" fill="none" stroke="#fff" stroke-width="1.5"/></svg></a>
    </article>
  </div>
</section>

<section class="news">
  <div class="news-head"><h2>お知らせ</h2><span>Information</span></div>
  <ul class="news-list">
    <li><time>2016.08.17</time>夏季休診日のお知らせを掲載しました</li>
    <li><time>2016.08.10</time>インフルエンザ予防接種の受付を開始しました</li>
    <li><time>2016.08.03</time>歯科の診療時間を一部変更いたします</li>
    <li><time>2016.07.26</time>整形外科の新しい医師が着任しました</li>
    <li><time>2016.07.12</time>ホームページをリニューアルしました</li>
  </ul>
</section>

<footer class="site-footer">
  <div class="footer-info">
    <div class="brand">
      <div class="brand-dot"></div>
      <div>
        <div class="brand-name">港みらいクリニック</div>
        <div class="brand-sub">内科・整形外科・歯科</div>
      </div>
    </div>
    <div class="footer-dept">診療科目<small>内科・整形外科・歯科</small></div>
    <p>診療時間｜午前 9:00〜12:30　午後 14:00〜18:00<br>土曜 9:00〜12:30<br>休診日｜日曜・祝日<br>〒231-0099 横浜市中区港央町4-2-8</p>
    <div class="phone-num"><svg width="32" height="32" viewBox="0 0 24 24"><path fill="#f08a1c" d="M6.6 10.8a15 15 0 0 0 6.6 6.6l2.2-2.2a1 1 0 0 1 1-.25 11.4 11.4 0 0 0 3.6.57 1 1 0 0 1 1 1V20a1 1 0 0 1-1 1A17 17 0 0 1 3 4a1 1 0 0 1 1-1h3.5a1 1 0 0 1 1 1c0 1.25.2 2.45.57 3.57a1 1 0 0 1-.25 1z"/></svg>045-555-0132</div>
    <table class="schedule">
      <thead><tr><th></th><th>月</th><th>火</th><th>水</th><th>木</th><th>金</th><th>土</th><th>日</th></tr></thead>
      <tbody>
        <tr><th>午前</th><td>●</td><td>●</td><td>●</td><td>●</td><td>●</td><td>●</td><td>－</td></tr>
        <tr><th>午後</th><td>●</td><td>●</td><td>●</td><td>●</td><td>●</td><td>－</td><td>－</td></tr>
      </tbody>
    </table>
  </div>
  <div class="map" role="img" aria-label="クリニック周辺の所在地を示す地図"></div>
</footer>

<nav class="footer-nav">
  <a href="#">ご挨拶・理念</a><a href="#">施設案内</a><a href="#">ドクター紹介</a><a href="#">アクセス</a><a href="#">よくある質問</a><a href="#">採用情報</a><a href="#">サイトマップ</a><a href="#">お問い合わせ</a><a href="#">予約</a>
</nav>
<div class="copyright">© 港みらいクリニック All Rights Reserved.</div>
</body>
</html>
```